Puristisch-modernes Webdesign für eine Anwaltskanzlei
Zielgruppe
Wir sind eine Patent- und Rechtsanwaltskanzlei mit Sitz in Frankfurt am Main, die inzwischen seit 15 Jahren besteht und den Fokus auf den 'Gewerblichen Rechtsschutz' und das Geistige Eigentum hat.
Unsere Kanzlei berät Mandanten ausführlich zu den Themen 'Patentrecht, Schutzstrategien, Patentanmeldung, Recherche, Geheimhaltungsvereinbarungen, Patentverletzung, Arbeitnehmererfindung und Streitverfahren'.
Unsere Kernzielgruppe kommt aus Deutschland bzw. der DACH-Region, ist männlich, zwischen 18 - 49 Jahren alt und technikaffin. Wir haben allerdings auch Mandanten aus China, der Türkei und den USA. Wir sprechen vorrangig mittlere und größere Unternehmen an.
Aufgabenstellung
Wir legen sehr viel wert auf eine hochwertige und puristische neue Homepage, die im Web 2.0 (oder gibt es heutzutage schon 3.0? ;-) ) angekommen ist. Sachen wie mobile-friendly sind für uns eine Selbstverständlichkeit. Das Thema "One-Pager" ist sicherlich klasse, aufgrund unseres Erklärungsbedarfs und bspw. den Anwalts-Vorstellungen scheidet dieser jedoch aus.
Wichtig: Wir würden gerne unsere aktuelle Link-Struktur beibehalten, damit wir aus SEO-Sicht keine Einbüße haben.
Um Ihnen Eindrücke zu geben, welche (unserer Meinung nach) positiven Beispiele es gibt, möchte ich Ihnen zwei Links mitgeben:
• http://deutschland.brennholtvarga.com (vor allem die Navigation und das Dropdown-Menü sehen sehr gut aus; auch das clean-e und puristische Design sind gut, Wording für EN/DE-Seite sehr gut - also dass es ausgeschrieben ist, bspw. "Deutsch" / "English" / "Chinese" / "Turkish"; Footer sehr schön strukturiert)
• http://www.weiler-lawfirm.com/home.html (Slider ist klasse, Social Media Buttons rechts oben gut eingebunden aber leider nicht im Chatterbook-Blau, Flitter-Blau, Zoogle-Rot etc. :-( , rechte Seite Veranstaltungen + Publikationen etc. gut)
• http://www.bromsel.de/ (Hier finden wir unten die Aufteilung in drei Blöcke sehr schön. Ggf. bei uns dann: "Die letzten Artikel" / "Über die Kanzlei" / "Unser Team")
Was noch unbedingt zu berücksichtigen ist: Wir haben einen sehr gut geführten und aktiven Blog (INFO.juris-vantor.com). Darein fließen auch viele Ressourcen.
Es ist sehr wohl denkbar, dass wir bereits auf der Kanzlei-Seite (WWW.juris-vantor.com) bspw. die letzten 3 deutschsprachigen und 3 englischsprachigen Artikel aufführen, um den User (auch) auf unseren Blog führen und quasi interne Verlinkungen machen.
Abschließend: Das Design soll auf das CMS "Wordpress" optimiert werden.

```html
<!DOCTYPE html>
<html lang="de">
<head>
<meta charset="utf-8">
<title>Kanzlei Startseite</title>
<link href="https://fonts.googleapis.com/css2?family=Roboto:wght@300;400;500;700&family=Roboto+Slab:wght@400&display=swap" rel="stylesheet">
<style>
:root{
  --orange:#e84e0f;
  --ink:#4a4a4a;
  --muted:#777;
  --page:#ffffff;
  --backdrop:#e6e6e6;
  --line:#dddddd;
}
*{box-sizing:border-box;margin:0;padding:0}
html,body{width:866px;height:1200px;overflow:hidden;background:var(--backdrop);font-family:'Roboto',sans-serif;color:var(--ink)}
.page{position:absolute;left:78px;top:0;width:709px;height:1200px;background:var(--page)}
.abs{position:absolute}
.brand{left:7px;top:6px;display:flex;align-items:center;gap:7px}
.brand-mark{width:25px;height:25px;background:var(--orange)}
.brand-name{font-family:'Roboto Slab',serif;font-size:7.5px;line-height:9px;color:var(--ink);letter-spacing:.3px}
.brand-name b{font-weight:400;color:var(--orange);display:block}
.lang{left:288px;top:10px;width:108px;height:16px;border:1px solid #e3e3e3;border-radius:9px;font-size:7.5px;line-height:14px;padding-left:12px;color:var(--ink);box-shadow:0 1px 2px rgba(0,0,0,.08)}
.lang i{font-style:italic}
.lang span{position:absolute;right:7px;font-size:5px;color:#999}
.nav{left:432px;top:14px;display:flex;gap:15px;font-size:7px;color:var(--muted)}
.nav .active{color:#333;font-weight:500}
.phone{left:604px;top:11px;display:flex;align-items:center;gap:6px;font-size:8.5px;font-weight:500;color:#444}
.blog{left:607px;top:38px;width:102px;height:19px;background:var(--orange);color:#fff;font-size:7px;font-weight:500;letter-spacing:.6px;line-height:19px;padding-left:6px}
.blog svg{position:absolute;right:7px;top:6px}
.social-side{left:682px;top:69px;display:flex;flex-direction:column;gap:3px}
.social-side span{width:14px;height:13px;background:#8a8a8a;border-radius:2px}
.hero-title{left:54px;top:68px;font-size:21px;font-weight:300;line-height:27px;color:#444}
.hero-title span{font-weight:400}
.hero{left:0;top:159px;width:709px;height:239px;background:linear-gradient(90deg,#6f4a34 0%,#8a5e41 30%,#7a5038 60%,#5c3d2c 100%)}
.quote{left:271px;top:80px;border-left:4px solid var(--orange);padding-left:13px;color:#fff;font-size:22px;font-weight:300;line-height:29px}
.quote-by{left:563px;top:133px;color:#fff;font-size:6.5px;font-weight:700}
.dots{left:335px;top:201px;display:flex;gap:7px}
.dots span{width:6px;height:6px;border-radius:50%;background:rgba(255,255,255,.55)}
.dots span:first-child{background:#fff}
.section-title{left:51px;top:446px;border-left:4px solid var(--orange);padding-left:11px;font-size:14.5px;line-height:19px;color:#444}
.card{top:515px;width:159px;height:232px;background:#fff;border:1px solid #e1e1e1}
.card.raised{box-shadow:0 5px 12px rgba(0,0,0,.12)}
.card-head{height:104px;background:var(--orange);color:#fff;padding:15px 18px;position:relative}
.card-head.photo{background:linear-gradient(135deg,#8b3f2a,#b24a2c 50%,#cf4a1e)}
.card-date{font-size:5px;font-weight:500}
.card-title{margin-top:13px;font-size:10.5px;line-height:14.5px}
.card-more{position:absolute;right:6px;bottom:6px;width:2px;height:8px;background:radial-gradient(circle,#fff 1px,transparent 1.2px) 0 0/2px 3px}
.card-body{padding:15px 18px 0;font-size:6.3px;line-height:11px;color:#444;height:97px}
.card-body a{color:var(--orange);font-style:italic;text-decoration:underline}
.card-foot{border-top:1px solid #eee;height:29px;display:flex;align-items:center;padding:0 9px;font-size:6.5px;color:#555;gap:5px}
.card-foot .shares{margin-left:auto;display:flex;gap:9px}
.card-foot .shares span{width:9px;height:9px;border-radius:50%;background:#555}
.rule{left:0;top:846px;width:709px;height:1px;background:#eee}
.awards{left:143px;top:872px;width:430px;display:flex;justify-content:space-between;align-items:center}
.award-round{width:36px;height:44px;border-radius:50%;}
.footer{left:0;top:944px;width:709px;height:256px;background:var(--orange);color:#fff}
.fcol-rule{top:65px;width:1px;height:191px;background:rgba(255,255,255,.25)}
.ftitle{top:72px;border-left:4px solid #fff;padding-left:11px;font-size:13px;line-height:18px}
.ftext{font-size:6.7px;line-height:11px}
.fbtn{border:1px solid #fff;font-size:6.7px;height:14px;line-height:12px;padding:0 7px;display:inline-block;margin-bottom:4px}
.fsocial{display:flex;gap:3px}
.fsocial span{width:15px;height:14px;background:#5a2a14;border-radius:2px}
</style>
</head>
<body>
<div class="page">
  <header>
    <div class="abs brand"><div class="brand-mark"></div><div class="brand-name">KLVORAX PATENT- &amp; RECHTSANWALTSKANZLEI<b>DR. KALVORAN &amp; PARTNERS LLP</b></div></div>
    <div class="abs lang">Deutsch | <i>Deutschland</i><span>▼</span></div>
    <nav class="abs nav"><span>Leistungen</span><span class="active">Kanzlei</span><span>Kontakt</span><span>Karriere</span></nav>
    <div class="abs phone"><svg width="14" height="14" viewBox="0 0 14 14"><circle cx="7" cy="7" r="6.3" fill="none" stroke="#555" stroke-width="1"/><path d="M4.6 4.2c.4-.4.9-.3 1.1.1l.5.9c.2.4 0 .7-.3.9.3.8.9 1.4 1.7 1.7.2-.3.5-.5.9-.3l.9.5c.4.2.5.7.1 1.1-1.6 1.4-5.4-2.3-4.9-4.9z" fill="#555"/></svg>0431 / 57 18 30 6</div>
    <div class="abs blog">BLOG<svg width="5" height="8" viewBox="0 0 5 8"><path d="M1 1l3 3-3 3" stroke="#fff" fill="none" stroke-width="1.2"/></svg></div>
    <div class="abs social-side" aria-label="Soziale Netzwerke"><span></span><span></span><span></span><span></span><span></span></div>
  </header>
  <h1 class="abs hero-title"><span>Wir beraten Sie</span><br>zu Patenten, Marken &amp; Designs</h1>
  <section class="abs hero" role="img" aria-label="Foto einer antiken Waage auf einem Holztisch vor unscharfem Bücherregal">
    <blockquote class="abs quote">The life of the law has not been logic;<br>it has been experience.</blockquote>
    <div class="abs quote-by">- Ansel W. Harlowe</div>
    <div class="abs dots"><span></span><span></span><span></span><span></span></div>
  </section>
  <h2 class="abs section-title" style="font-weight:400">Neuigkeiten</h2>

  <article class="abs card" style="left:102px">
    <div class="card-head"><div class="card-date">3. Juni 2016</div><div class="card-title">Was genau ist<br>eigentlich ein<br>Gebrauchsmuster?</div><div class="card-more"></div></div>
    <div class="card-body">Was genau verbirgt sich hinter dem Begriff Gebrauchsmuster? Und warum wird das Gebrauchsmuster kleiner Bruder des Patents genannt? Was es schützt, was es bringt und wann Sie es nutzen können... <a>weiterlesen</a></div>
    <div class="card-foot"><svg width="12" height="10" viewBox="0 0 12 10"><rect x=".5" y=".5" width="11" height="9" rx="1.5" fill="none" stroke="#666"/><path d="M3 3.5h6M3 5h6M3 6.5h4" stroke="#666" stroke-width=".8"/></svg>3<div class="shares"><span></span><span></span><span></span></div></div>
  </article>
  <article class="abs card raised" style="left:273px">
    <div class="card-head"><div class="card-date">3. Juni 2016</div><div class="card-title">Dr. Kalvoran<br>&amp; Partners LLP schützt<br>Marke „Aerion“</div><div class="card-more"></div></div>
    <div class="card-body">Die NORVELT AERO GmbH aus Hohentengen hat mit der Patent- und Rechtsanwaltskanzlei Dr. Kalvoran &amp; Partners LLP erfolgreich die Schutzrechte...<br><a>weiterlesen</a></div>
    <div class="card-foot"><svg width="12" height="10" viewBox="0 0 12 10"><rect x=".5" y=".5" width="11" height="9" rx="1.5" fill="none" stroke="#666"/><path d="M3 3.5h6M3 5h6M3 6.5h4" stroke="#666" stroke-width=".8"/></svg>3<div class="shares"><span></span><span></span><span></span></div></div>
  </article>
  <article class="abs card" style="left:444px">
    <div class="card-head photo" role="img" aria-label="Bunte Tastatur mit Markensymbolen"><div class="card-date">3. Juni 2016</div><div class="card-title">Eine Marke anmelden:<br>Diese Basics MÜSSEN<br>Sie wissen – Teil 1</div><div class="card-more"></div></div>
    <div class="card-body">Was genau verbirgt sich hinter dem Begriff Gebrauchsmuster? Und warum wird das Gebrauchsmuster kleiner Bruder des Patents genannt? Was es schützt, was es bringt und wann Sie es nutzen können... <a>weiterlesen</a></div>
    <div class="card-foot"><svg width="12" height="10" viewBox="0 0 12 10"><rect x=".5" y=".5" width="11" height="9" rx="1.5" fill="none" stroke="#666"/><path d="M3 3.5h6M3 5h6M3 6.5h4" stroke="#666" stroke-width=".8"/></svg>3<div class="shares"><span></span><span></span><span></span></div></div>
  </article>

  <div class="abs rule"></div>
  <div class="abs awards" aria-label="Auszeichnungen">
    <div class="award-round" style="background:#3aa99a"></div>
    <div style="width:26px;height:38px;background:#b8962a"></div>
    <div class="award-round" style="background:#c3a245"></div>
    <div style="width:37px;height:20px;background:#222"></div>
    <div class="award-round" style="background:#9a2b86"></div>
    <div style="width:38px;height:21px;border:1px solid #bbb;background:#f6f6f6"></div>
  </div>

  <footer class="abs footer">
    <div class="abs fcol-rule" style="left:260px"></div>
    <div class="abs fcol-rule" style="left:430px"></div>
    <h3 class="abs ftitle" style="left:102px;font-weight:400">Kontakt</h3>
    <h3 class="abs ftitle" style="left:274px;font-weight:400">Service</h3>
    <h3 class="abs ftitle" style="left:444px;font-weight:400">Folgen Sie Uns</h3>
    <div class="abs ftext" style="left:117px;top:112px">Lindenhofstr. 12-14<br>D-60311 Frankfurt am Main<br>Deutschland – Germany<br><br>Tel: +49 (0) 69 / 413 905 - 0<br>Fax: +49 (0) 69 / 413 905 - 199<br>info@juris-vantor.com</div>
    <div class="abs" style="left:285px;top:109px;width:130px">
      <span class="fbtn">Fordern Sie einen Rückruf an</span>
      <span class="fbtn">Informationen für sichere E-Mails</span>
      <span class="fbtn">Sitemap</span><br>
      <span class="fbtn">ISO-Zertifikat</span>
    </div>
    <div class="abs fsocial" style="left:459px;top:110px" aria-label="Soziale Netzwerke"><span></span><span></span><span></span><span></span><span></span></div>
  </footer>
</div>
</body>
</html>
```